Präsentationsvorlagen / Powerpoint Master for my company
Zielgruppe
Offline hardware device to manage and save passwords safely.
Aufgabenstellung
DIN A4 quer

```html
<!DOCTYPE html>
<html lang="en">
<head>
<meta charset="utf-8">
<title>LockVale – Presentation Master</title>
<link href="https://fonts.googleapis.com/css2?family=Poppins:wght@400;500;600;700&display=swap" rel="stylesheet">
<style>
:root{
  --stage:#41b86f;
  --brand:#0a7d34;
  --brand-deep:#007a33;
  --yellow:#ffe800;
  --ink:#1b1b1b;
  --white:#ffffff;
  --rule:#cfcfcf;
}
*{margin:0;padding:0;box-sizing:border-box}
html,body{width:1200px;height:849px;overflow:hidden}
body{background:var(--stage);font-family:'Poppins',sans-serif;color:var(--ink);position:relative}
.slide{position:absolute;width:340px;height:191px;background:var(--white);overflow:hidden}
.c1{left:60px}.c2{left:430px}.c3{left:800px}
.r1{top:103px}.r2{top:326px}.r3{top:554px}
.abs{position:absolute}
.glow-yellow{position:absolute;border-radius:50%;background:radial-gradient(closest-side,var(--yellow) 0%,rgba(255,232,0,.6) 45%,rgba(255,232,0,0) 100%)}
.glow-green{position:absolute;border-radius:50%;background:radial-gradient(closest-side,var(--brand) 0%,rgba(10,125,52,.55) 45%,rgba(10,125,52,0) 100%)}
.card{position:absolute;background:var(--white)}
.num{font-weight:600;color:var(--brand);font-size:9px}
.head{font-weight:700;color:var(--brand);line-height:1.15}
.body{font-size:5.6px;line-height:1.35;color:var(--ink)}
.photo{position:absolute}
.wordmark{font-weight:700;color:var(--brand);letter-spacing:.3px;display:flex;align-items:center;gap:4px}
.wordmark .dot{width:.7em;height:.7em;border-radius:50%;background:currentColor;display:inline-block}
/* cover */
.cover .wordmark{left:30px;top:16px;font-size:15px}
.cover .title{left:30px;top:58px;font-size:20.5px}
.cover .sub{left:30px;top:121px;font-size:11px}
.cover .date{left:30px;top:147px;font-size:6.5px}
/* feature icons */
.feature{position:absolute;top:80px;width:64px}
.feature svg{display:block;height:21px}
.feature .label{font-size:6px;color:var(--brand);margin-top:10px}
.feature .body{font-size:4.6px;margin-top:9px}
/* team */
.member{position:absolute;top:47px;width:69px;height:102px;background:var(--white)}
.member .photo{left:0;top:0;width:69px;height:62px}
.member .name{position:absolute;left:4px;top:64px;font-size:6px;color:var(--brand)}
.member .role{position:absolute;left:4px;top:72px;font-size:4.2px;color:var(--brand)}
.member .note{position:absolute;left:4px;top:81px;font-size:3.6px;font-weight:500;line-height:1.3}
/* strategy */
.col-text{position:absolute;top:125px;width:95px;font-size:3.6px;line-height:1.35;text-align:justify}
</style>
</head>
<body>

<!-- Cover -->
<section class="slide c1 r1 cover">
  <div class="glow-yellow" style="left:150px;top:-40px;width:260px;height:230px"></div>
  <div class="glow-green" style="left:-10px;top:110px;width:230px;height:170px"></div>
  <div class="wordmark abs"><span class="dot"></span>LockVale</div>
  <h1 class="head abs title">Hardware<br>Device</h1>
  <p class="abs sub">manage and save passwords</p>
  <p class="abs date">October 2023</p>
</section>

<!-- 01 -->
<section class="slide c2 r1">
  <div class="glow-yellow" style="left:0;top:-70px;width:300px;height:150px"></div>
  <div class="glow-green" style="left:290px;top:110px;width:90px;height:110px"></div>
  <div class="card" style="left:21px;top:55px;width:298px;height:137px">
    <p class="num abs" style="left:24px;top:17px">01</p>
    <h2 class="head abs" style="left:24px;top:36px;font-size:9.5px">What is data integration ?</h2>
    <p class="body abs" style="left:24px;top:58px;width:232px">Branding is defined as the process of coming up or making a unique name or design for a certain product.</p>
    <p class="body abs" style="left:24px;top:81px;width:232px">Having a good brand strategy allows you to have a major advantage in gaining a large increase in your market competitions. Your brand tells your customers what they can expect from the products and services you offer.</p>
  </div>
</section>

<!-- 02 -->
<section class="slide c3 r1">
  <div class="glow-yellow" style="left:-40px;top:-30px;width:260px;height:200px"></div>
  <div class="glow-green" style="left:40px;top:130px;width:150px;height:110px"></div>
  <p class="num abs" style="left:21px;top:31px">02</p>
  <h2 class="head abs" style="left:21px;top:53px;font-size:9.5px">Data literacy</h2>
  <p class="body abs" style="left:21px;top:79px;width:142px;text-align:justify">Are you innovative or are you the experienced type? Do you offer a high-cost, high-quality product, or a low-cost, high-value product? It's impossible to be both. You should consider thinking what your customers need you to be. Your logo is the main foundation of your brand. All the promotional materials should be connected with your logo to communicate with your brand.</p>
  <div class="photo" role="img" aria-label="Hands typing on a laptop showing analytics charts" style="left:184px;top:0;width:156px;height:191px;background:linear-gradient(135deg,#d9d6d0,#a9a6a2 55%,#5e5a57)"></div>
</section>

<!-- 03 -->
<section class="slide c1 r2">
  <div class="glow-yellow" style="left:170px;top:-30px;width:220px;height:200px"></div>
  <div class="glow-green" style="left:50px;top:120px;width:220px;height:120px"></div>
  <div class="card" style="left:38px;top:38px;width:170px;height:114px">
    <p class="abs" style="left:16px;top:14px;font-size:8.5px;color:var(--brand)">03</p>
    <h2 class="head abs" style="left:16px;top:34px;font-size:12.5px">Preparation<br>is key</h2>
    <div class="abs" style="left:16px;top:76px;width:140px;height:1px;background:var(--rule)"></div>
    <p class="body abs" style="left:16px;top:84px;width:140px;font-size:6.2px">How to structure your organization for data integration</p>
  </div>
  <div class="photo" role="img" aria-label="Mechanical keyboard on a wooden desk" style="left:208px;top:39px;width:90px;height:113px;background:linear-gradient(160deg,#b9aa97,#8f806f 45%,#3a3a3c 70%,#a99a88)"></div>
</section>

<!-- Text with team photo -->
<section class="slide c2 r2">
  <div class="photo" role="img" aria-label="Team in a meeting with a woman placing sticky notes on a wall" style="left:0;top:0;width:340px;height:85px;background:linear-gradient(90deg,#cfcfcf,#4b4b4f 30%,#e9e8e5 55%,#d9c79a 70%,#3b3b3e 100%)"></div>
  <p class="body abs" style="left:21px;top:104px;width:263px;font-size:5.9px">Brand messages are delivered and planned based on the questions how, what, when, to whom and where your brand strategy is. Advertisement, visual communication, and distribution channels are parts of brand strategy.</p>
  <p class="body abs" style="left:21px;top:134px;width:263px;font-size:5.9px">The branding strategy you have should be consistent as it leads to a strong brand equity.</p>
</section>

<!-- Features -->
<section class="slide c3 r2">
  <div class="glow-yellow" style="left:0;top:-70px;width:320px;height:150px"></div>
  <div class="glow-green" style="left:300px;top:100px;width:80px;height:120px"></div>
  <div class="card" style="left:21px;top:55px;width:319px;height:136px"></div>
  <div class="feature" style="left:54px">
    <svg viewBox="0 0 36 22" width="36" fill="none" stroke="#0a7d34" stroke-width="1">
      <rect x="1" y="1" width="28" height="20"/><line x1="1" y1="5" x2="29" y2="5"/>
      <rect x="4" y="8" width="9" height="9"/><rect x="15" y="8" width="8" height="9"/>
      <line x1="24" y1="9" x2="27" y2="9"/><line x1="24" y1="12" x2="27" y2="12"/>
      <path d="M31 16l3 3-1 0 1 2"/>
    </svg>
    <p class="label">Data analysis</p>
    <p class="body">The branding strategy you have should be consistent as it leads to a strong brand equity.</p>
  </div>
  <div class="feature" style="left:142px">
    <svg viewBox="0 0 30 22" width="30" fill="none" stroke="#0a7d34" stroke-width="1">
      <rect x="9" y="1" width="12" height="5"/><line x1="15" y1="6" x2="15" y2="10"/>
      <rect x="4" y="10" width="22" height="4"/>
      <line x1="6" y1="14" x2="6" y2="16"/><line x1="15" y1="14" x2="15" y2="16"/><line x1="24" y1="14" x2="24" y2="16"/>
      <path d="M6 16l3 3-3 3-3-3z"/><path d="M15 16l3 3-3 3-3-3z"/><path d="M24 16l3 3-3 3-3-3z"/>
    </svg>
    <p class="label">Algorithm</p>
    <p class="body">The branding strategy you have should be consistent as it leads to a strong brand equity.</p>
  </div>
  <div class="feature" style="left:229px">
    <svg viewBox="0 0 30 22" width="30" fill="none" stroke="#0a7d34" stroke-width="1">
      <circle cx="8" cy="7" r="4"/><circle cx="8" cy="7" r="1.6"/><circle cx="8" cy="7" r="6" stroke-dasharray="2 1.8"/>
      <circle cx="20" cy="14" r="5"/><circle cx="20" cy="14" r="2"/><circle cx="20" cy="14" r="7.2" stroke-dasharray="2.4 2"/>
    </svg>
    <p class="label">Management</p>
    <p class="body">The branding strategy you have should be consistent as it leads to a strong brand equity.</p>
  </div>
</section>

<!-- Strategy -->
<section class="slide c1 r3">
  <div class="abs" style="left:0;top:176px;width:340px;height:14px;background:linear-gradient(90deg,rgba(10,125,52,0) 0%,#0a7d34 12%,#7fc85a 45%,var(--yellow) 80%,rgba(255,232,0,0) 100%);border-radius:50%;filter:blur(3px)"></div>
  <div class="photo" role="img" aria-label="Hand sketching a diagram on a whiteboard" style="left:21px;top:25px;width:95px;height:84px;background:linear-gradient(135deg,#efefed,#d6d6d3 60%,#b7a89b)"></div>
  <div class="photo" role="img" aria-label="Two colleagues planning at a whiteboard with a laptop" style="left:122px;top:25px;width:95px;height:84px;background:linear-gradient(135deg,#5a4a40,#e8e7e3 45%,#d2d0cb 75%,#6b5e55)"></div>
  <div class="photo" role="img" aria-label="Smart speaker next to a phone on a table" style="left:224px;top:25px;width:95px;height:84px;background:linear-gradient(135deg,#e4e4e2,#3d3f44 45%,#c9cacb 75%,#f0f0ef)"></div>
  <h3 class="abs" style="left:21px;top:124px;font-size:7px;font-weight:500">Data integration strategy</h3>
  <p class="col-text" style="left:21px;top:135px">It is a process to allow an organization to focus resources on the greatest opportunities to increase sales and achieve the company's target.</p>
  <p class="col-text" style="left:122px">Marketing strategy's goal is to increase sales and achieve the advantage over other competitions. It includes short term and long term activities of marketing that has to do with the analysis of a company's situation and contribute to its objectives.</p>
  <p class="col-text" style="left:224px">The objectives will be based on how you gain sales by acquiring and keeping customers. A marketing strategy helps convey effective messages with the right twist of marketing approaches that will maximize your sales outcome and marketing activities.</p>
</section>

<!-- Team -->
<section class="slide c2 r3">
  <div class="glow-yellow" style="left:60px;top:-60px;width:260px;height:140px"></div>
  <div class="glow-green" style="left:270px;top:120px;width:110px;height:110px"></div>
  <h2 class="head abs" style="left:21px;top:15px;font-size:9.5px">Meet our founding team</h2>
  <div class="member" style="left:21px">
    <div class="photo" role="img" aria-label="Portrait of the CEO" style="background:linear-gradient(180deg,#f3f1ee,#d9c3b3 70%,#c9b2a2)"></div>
    <p class="name">Liora</p><p class="role">CEO</p><p class="note">~ Co-founder at Companyname</p>
  </div>
  <div class="member" style="left:97px">
    <div class="photo" role="img" aria-label="Portrait of the CTO" style="background:linear-gradient(180deg,#f3f3f3,#d8bfae 55%,#5b6f8e)"></div>
    <p class="name">Tobin</p><p class="role">CTO</p><p class="note">~ Co-founder at Companyname</p>
  </div>
  <div class="member" style="left:173px">
    <div class="photo" role="img" aria-label="Portrait of the chief engineer" style="background:linear-gradient(180deg,#f2f2f2,#5a3d30 55%,#2c211c)"></div>
    <p class="name">Maren</p><p class="role">Chief Engineer</p>
  </div>
  <div class="member" style="left:250px">
    <div class="photo" role="img" aria-label="Portrait of the business developer" style="background:linear-gradient(180deg,#f2f2f2,#b98c76 55%,#7a2a2a)"></div>
    <p class="name">Silas</p><p class="role">Business Dev.</p><p class="note">~ Entrepreneur at Companyname<br>~ Project manager</p>
  </div>
</section>

<!-- Closing -->
<section class="slide c3 r3" style="background:var(--brand-deep);color:var(--white)">
  <h2 class="abs" style="left:21px;top:78px;font-size:12.5px;font-weight:700">Thank you.</h2>
  <div class="wordmark abs" style="left:21px;top:121px;font-size:15px;color:var(--white)"><span class="dot"></span>LockVale</div>
  <p class="abs" style="left:21px;top:144px;font-size:3.8px;line-height:1.3">123 Address, road, city, country 0000<br>+00 000 0000<br>lockvale.com<br>info@lockvale.com</p>
  <p class="abs" style="left:21px;top:170px;font-size:3.8px">All rights reserved for technology template</p>
</section>

</body>
</html>
```